I am looking for help designing my new business cards. I would like rounded edges and a raised logo on the back of the card. I have 2 Logos. One with a boat in it and one without. I'd like the one on the back to be the one that includes the boat and just the name on the front. I have included multiple formats of my logo. Please let me know if you need anymore.

Target Market(s)

Potential buyers and other sales brokers

Industry/Entity Type

Sales - Yacht / Boat Sales

Contact Information for Business Card

Id liike the front to include just the business name portion of the logo along with my name (Corwin Dalby), phone number (555.318.6027), website address (www.dalbymarineco.example) and not my physical address but just "Charleston, SC". The back should include my full logo that has the boat included. This portion I'd prefer raised amd take up the majority of the space there. Thanks!!

Colors
0054AA
0677BA
7BADD7
CADEEF
E8F1F8
0094D4
00A9DD
6FCCEA
C7EBF8
E9F6FB

Requirements
Must have
• Double sided
Nice to have
• My email address: Corwin@dalbymarineco.example The NMTG logo somewhere small on the front of the card
Should not have
• My full address, prefer only "Charleston, SC"

```html
<!DOCTYPE html>
<html lang="en">
<head>
<meta charset="utf-8">
<title>Dalby Marine Co. business card</title>
<link href="https://fonts.googleapis.com/css2?family=Montserrat:wght@400;700;800&display=swap" rel="stylesheet">
<style>
  :root {
    --navy: #001a5c;
    --brand-blue: #0054aa;
    --sky: #0094d4;
    --paper: #ffffff;
    --backdrop: #c9c9cb;
    --shadow: rgba(0, 0, 0, 0.18);
  }
  * { margin: 0; padding: 0; box-sizing: border-box; }
  html, body {
    width: 1200px; height: 900px; overflow: hidden;
    background: var(--backdrop);
    font-family: "Montserrat", sans-serif;
    color: var(--navy);
  }
  .sheet {
    position: relative; width: 1200px; height: 900px;
    display: flex; flex-direction: column; align-items: center; justify-content: center; gap: 40px;
  }
  .card {
    position: relative; width: 560px; height: 320px;
    background: var(--paper); border-radius: 16px; overflow: hidden;
    box-shadow: 0 10px 24px var(--shadow);
  }
  .card-art { position: absolute; inset: 0; width: 100%; height: 100%; }

  /* front */
  .holder-name { position: absolute; left: 44px; top: 38px; font-size: 24px; font-weight: 700; }
  .contact-list { position: absolute; left: 44px; top: 84px; list-style: none; }
  .contact-item { display: flex; align-items: center; gap: 10px; font-size: 14.5px; margin-bottom: 7px; }
  .contact-icon { width: 20px; height: 20px; flex: none; }
  .front-wordmark {
    position: absolute; left: 48px; top: 246px;
    font-size: 21px; font-weight: 800; color: var(--brand-blue); letter-spacing: 0.04em; text-transform: uppercase;
  }

  /* back */
  .back-mark {
    position: absolute; left: 0; right: 0; top: 70px;
    display: flex; align-items: center; justify-content: center; gap: 14px;
  }
  .back-dot { width: 26px; height: 26px; border-radius: 50%; background: var(--sky); }
  .back-wordmark {
    font-size: 38px; font-weight: 800; color: var(--brand-blue); letter-spacing: 0.04em; text-transform: uppercase;
  }
</style>
</head>
<body>
<main class="sheet">
  <section class="card card-front" aria-label="Card front">
    <svg class="card-art" viewBox="0 0 560 320" aria-hidden="true">
      <polygon points="0,206 560,196 560,320 0,320" fill="var(--navy)"/>
      <polygon points="14,214 330,208 330,320 14,320" fill="var(--paper)"/>
      <polygon points="336,208 560,204 560,320 336,320" fill="var(--navy)"/>
    </svg>
    <h1 class="holder-name">Corwin Dalby</h1>
    <ul class="contact-list">
      <li class="contact-item">
        <svg class="contact-icon" viewBox="0 0 20 20"><rect width="20" height="20" fill="var(--navy)"/><path d="M10 4a4 4 0 0 0-4 4c0 3 4 8 4 8s4-5 4-8a4 4 0 0 0-4-4zm0 5.5a1.5 1.5 0 1 1 0-3 1.5 1.5 0 0 1 0 3z" fill="#fff"/></svg>
        Gullport, SC.
      </li>
      <li class="contact-item">
        <svg class="contact-icon" viewBox="0 0 20 20"><rect width="20" height="20" fill="var(--navy)"/><path d="M6 4l2.5 0 1 3-1.5 1.2a8 8 0 0 0 3.8 3.8L13 10.5l3 1V14a2 2 0 0 1-2 2A10 10 0 0 1 4 6a2 2 0 0 1 2-2z" fill="#fff"/></svg>
        555.318.6027
      </li>
      <li class="contact-item">
        <svg class="contact-icon" viewBox="0 0 20 20"><rect width="20" height="20" fill="var(--navy)"/><rect x="4" y="6" width="12" height="8" fill="none" stroke="#fff" stroke-width="1.3"/><path d="M4 6l6 5 6-5" fill="none" stroke="#fff" stroke-width="1.3"/></svg>
        corwin@dalbymarineco.example
      </li>
      <li class="contact-item">
        <svg class="contact-icon" viewBox="0 0 20 20"><rect width="20" height="20" fill="var(--navy)"/><circle cx="10" cy="10" r="6" fill="none" stroke="#fff" stroke-width="1.2"/><ellipse cx="10" cy="10" rx="2.6" ry="6" fill="none" stroke="#fff" stroke-width="1.1"/><path d="M4 10h12" stroke="#fff" stroke-width="1.1"/></svg>
        www.dalbymarineco.example
      </li>
    </ul>
    <p class="front-wordmark">Dalby Marine Co.</p>
  </section>

  <section class="card card-back" aria-label="Card back">
    <svg class="card-art" viewBox="0 0 560 320" aria-hidden="true">
      <polygon points="0,190 560,230 560,320 0,320" fill="var(--navy)"/>
    </svg>
    <div class="back-mark">
      <span class="back-dot"></span>
      <p class="back-wordmark">Dalby Marine Co.</p>
    </div>
  </section>
</main>
</body>
</html>
```